Tilly the Otter - Kids (2-5years) - ALL NATURAL - Bath & Body Skincare - Label / Packaging Design

Carnwick Heather Estate is the owner of the 'celebrity' lavender bear, Tilly the Otter. Carnwick is the world largest commercial lavender farm and home to the world finest lavender, lavender oil and skincare products. www.carnwickheather-example.com

We are launching a line of Kids skincare products targeted to the Australian and China market (where Tilly is considered a superstar/celebrity).

All natural products made in Australia:

We are looking for 3-4 few packaging concept designs for packaging for our Tilly Kids - Bath, Body & Bed Range.

The "Tilly Kids" Toiletry Range includes:
= Shampoo/Bath Gel
= Fizzy Bath Bombs
= Moisturiser
= Pillow Spray (together aka the “Tilly Snoozetime Routine”)

= Later, possible additions to the Tilly the Otter range include the below items so the conceptual design must be adaptable.
- Bath robe
- Bed Linen Sets
- Crockey sets

See Filecrate folder here for all image and brand information:
https://www.filecrate-example.com/sh/8kqmvr2tw9x3hn1/QQpzrLmeTdFgYh7kWsVuXcA2b?dl=0

Note: There are some current DRAFT concept created by another designer in the image section of the brief. These are NOT ready or high quality enough (and too dull and busy) but will give you a good reference for what we don't want (too dark/busy/illegible). Please create new ideas....
Updates

HI - NEW FILECRATE FILE LINK IN CASE THE ONE I SENT PREVIOUSLY IS NOT WORKING - https://www.filecrate-example.com/sh/8kqmvr2tw9x3hn1/QQpzrLmeTdFgYh7kWsVuXcA2b?dl=0IVE ALSO ADDED A FEW NEW FILES... Added Wednesday, June 14, 2017

Pls see links to Penrick's and TOTs Organic... http://www.boxdesignshowcase-example.com/2017/02/tots-organic.html https://www.penricksorganic-example.com.au We asked our social media agency in china for their thoughts on the colour scheme's so far (not including new attempts here) and they said the following: "From our perspective - we agree that the colour hues are not quite right - and while we love Tilly, we wonder whether the current design and packaging options doesn't quite reflect the premium price points that you want to position these products. We are aware that you are limited with a certain number of packaging options but worry that the pale and purple colours may not attract Chinese parents. While sunscreen is not a premium product - please see the Chasing Wren package that one of our clients has had strong sales in China https://www.sunsafeshop-example.org.au/product/wren-splash-play-sunscreen.html In short, the Tilly design needs to be colourful, rich and vibrant in our opinion"

Target Market(s)

Children 2-5 years old. Primarily young Australian and Chinese mothers and their children.

Industry/Entity Type

Farm

Font styles to use
Other font styles liked:
• Topik px is the main wordmark font. The copy font is your choice.

Requirements
Must have
• Specifically, a general Packaging Design that can be used across a wide range of products and packaging types.
• Packaging & Visual Design –Important Considerations:
• Please be creative!
• •Please ensure the design can be used as a (waterproof) label or printed on the bottle...
• • Please show the design on various bottle sizes and colours (clear, white, cream etc)
• • Please suggest various eco-friendly bottle material (PBS free recyclable plastic)?
• • Must have multi-country / cultural appeal
• Must be polished, fun, western/australian design standard but also appeals to Chinese design tastes..
• Feel free to add some splashes of kid-friendly colours - blues, pinks, yellow, greens etc
• See Filecrate folder here for all image and brand information:
• https://www.filecrate-example.com/sh/8kqmvr2tw9x3hn1/QQpzrLmeTdFgYh7kWsVuXcA2b?dl=0
• Notes from our contracts manufacturer:
• "For the tube there will be limitation to the puck size, this is the opening diameter of the tube. On the tube you are not able to print 6mm from the top of the tube closure when printing. For sticker application on the tube you will need to allow for spacing on each edge to ensure there is no creasing"
• The current budget covers the overall concept and (and 1 x packaging completed) We are willing to negotiate an additional small cost for the extra 2-3 product specific designs.
• We expect print ready packaging and we will supply the dielines to the chosen designer once we have decided upon the exact size, style and approach for the packaging - printing or labels (this part might take a few weeks as we need to review our options) but we can release (part) payment before if required.
Should not have
• No brown-bottles please.

```html
<!DOCTYPE html>
<html lang="en">
<head>
<meta charset="utf-8">
<title>Tilly Kids – Bath &amp; Body Label</title>
<link rel="stylesheet" href="https://fonts.googleapis.com/css2?family=Bubblegum+Sans&display=swap">
<style>
  :root {
    --backdrop: #d9d9d9;
    --label-pink: #e8336f;
    --label-pink-deep: #d21f63;
    --brand-purple: #6a3a98;
    --badge-purple: #7b4aa8;
    --edge-white: #ffffff;
    --ink-white: #ffffff;
    --ink-outline: #5a2a6e;
    --photo-lilac: #a48ad6;
    --photo-violet: #7c62bb;
    --pattern-magenta: #c0246a;
    --pattern-purple: #5d2d8a;
  }
  html, body {
    margin: 0;
    padding: 0;
    width: 1200px;
    height: 1200px;
    overflow: hidden;
    background: var(--backdrop);
  }
  .canvas {
    position: relative;
    width: 1200px;
    height: 1200px;
    background: radial-gradient(ellipse at 50% 40%, #ececec 0%, var(--backdrop) 75%);
  }
  .label {
    position: absolute;
    left: 80px;
    top: 270px;
    width: 1040px;
    height: 660px;
    box-sizing: border-box;
    border-top: 14px solid var(--edge-white);
    border-bottom: 14px solid var(--edge-white);
    background: radial-gradient(ellipse at 50% 55%, var(--label-pink) 0%, var(--label-pink-deep) 100%);
    overflow: hidden;
    font-family: "Bubblegum Sans", cursive;
  }
  .brand-badge {
    position: absolute;
    left: 560px;
    top: 10px;
    width: 200px;
    height: 200px;
    border-radius: 50%;
    background: var(--brand-purple);
    display: flex;
    flex-direction: column;
    align-items: center;
    justify-content: center;
    color: var(--ink-white);
    text-align: center;
  }
  .brand-name {
    font-size: 18px;
    letter-spacing: 3px;
    line-height: 1;
    margin-right: 24px;
  }
  .range-name {
    font-size: 44px;
    line-height: 1;
    margin-right: 24px;
    margin-top: 4px;
  }
  .size-badge {
    position: absolute;
    left: 730px;
    top: 70px;
    width: 74px;
    height: 74px;
    border-radius: 50%;
    background: var(--badge-purple);
    color: var(--ink-white);
    font-size: 21px;
    display: flex;
    align-items: center;
    justify-content: center;
  }
  .product-name {
    position: absolute;
    left: 0;
    right: 0;
    top: 215px;
    margin: 0;
    text-align: center;
    font-weight: 400;
    font-size: 108px;
    line-height: 1;
    color: var(--ink-white);
    letter-spacing: 2px;
    -webkit-text-stroke: 3px var(--ink-outline);
    paint-order: stroke fill;
  }
  .tagline {
    position: absolute;
    left: 0;
    right: 0;
    top: 335px;
    margin: 0;
    text-align: center;
    font-size: 26px;
    color: var(--ink-white);
    letter-spacing: 2px;
  }
  .mascot-photo {
    position: absolute;
    left: 370px;
    top: 385px;
    width: 330px;
    height: 275px;
    border-radius: 150px 150px 0 0;
    background: radial-gradient(ellipse at 50% 45%, var(--photo-lilac) 0%, var(--photo-violet) 100%);
  }
  .pattern-strip {
    position: absolute;
    top: 470px;
    width: 220px;
    height: 190px;
    background: linear-gradient(135deg, var(--pattern-magenta) 0%, var(--pattern-purple) 100%);
  }
  .pattern-strip--left { left: 150px; }
  .pattern-strip--right { left: 700px; }
</style>
</head>
<body>
  <main class="canvas">
    <section class="label">
      <div class="brand-badge">
        <span class="brand-name">CARNWICK</span>
        <span class="range-name">kids</span>
      </div>
      <div class="size-badge">250ML</div>
      <h1 class="product-name">TILLY KIDS</h1>
      <p class="tagline">- BATH &amp; BODY WASH -</p>
      <div class="pattern-strip pattern-strip--left" role="img" aria-label="Decorative zigzag pattern in magenta, purple and white"></div>
      <div class="pattern-strip pattern-strip--right" role="img" aria-label="Decorative zigzag pattern in magenta, purple and white"></div>
      <div class="mascot-photo" role="img" aria-label="Photo of the purple plush mascot, Tilly"></div>
    </section>
  </main>
</body>
</html>
```